New counselling and hypnotherapy business

I'd like a flyer which is relevant to people who want support and to improve their wellbeing which follows the same theme as my website: http://larkmoretherapy.plumweave.com
And emphasise that whatever the area of concern, development or growth and I can tailor my knowledge and skills to help.

I'd like to use the same logo and my emphasis is to draw the audience in...therapy and counselling is for people who are "stuck" and having a difficult time...it can also be useful has a personal development tool.

Hypnotherapy

```html
<!DOCTYPE html>
<html lang="en">
<head>
<meta charset="utf-8">
<title>Larkmore Counselling &amp; Hypnotherapy – Trifold Flyer</title>
<link href="https://fonts.googleapis.com/css2?family=Cinzel:wght@400&family=Crimson+Text:wght@400;600&family=PT+Sans:ital,wght@0,400;0,700;1,400&display=swap" rel="stylesheet">
<style>
  :root {
    --backdrop: #e8e5e1;
    --plum: #4b2b4d;
    --plum-deep: #381f3a;
    --plum-soft: #6c4770;
    --green: #2f9d45;
    --paper: #ffffff;
    --ink-plum: #4a2a55;
    --text-light: #f1eaf2;
  }
  * { box-sizing: border-box; margin: 0; padding: 0; }
  html, body { width: 1200px; height: 848px; overflow: hidden; }
  body { background: var(--backdrop); font-family: "PT Sans", sans-serif; }

  .canvas { position: relative; width: 1200px; height: 848px; overflow: hidden; background: var(--backdrop); }

  .spread {
    position: absolute; top: 216px; width: 588px; height: 416px;
    display: flex; box-shadow: 0 4px 14px rgba(0,0,0,.25);
  }
  .spread--outside { left: 8px; }
  .spread--inside { left: 604px; }

  .panel { position: relative; width: 196px; height: 100%; overflow: hidden; color: var(--text-light); }
  .panel--plum { background: var(--plum); }
  .panel--paper { background: var(--paper); color: var(--ink-plum); }

  .copy { font-size: 5.6px; line-height: 1.3; padding: 0 6px; margin-bottom: 4px; }
  .copy em { font-style: italic; }
  .copy strong { font-weight: 700; }

  .band-heading {
    background: var(--plum-deep); color: #fff; font-weight: 700;
    font-size: 7.2px; letter-spacing: .2px; text-transform: uppercase;
    padding: 3px 6px; margin: 6px 0 4px;
  }
  .band-heading--soft {
    background: var(--plum-soft); border-radius: 3px 3px 0 0;
    text-align: center; margin: 6px 6px 5px;
  }

  .photo { display: block; }
  .photo--lounge { height: 72px; background: linear-gradient(135deg, #d9c7a8 0%, #8c6a4a 45%, #2b211c 100%); }
  .photo--room { height: 70px; background: linear-gradient(160deg, #efe4cf 0%, #cdb48c 55%, #8b7a4d 100%); }
  .photo--portrait {
    position: absolute; left: 4px; top: 262px; width: 64px; height: 154px;
    background: linear-gradient(180deg, #c9b59a 0%, #b9705e 50%, #8a2e32 100%);
  }

  /* outside spread artwork */
  .wave-art { position: absolute; left: 196px; top: 112px; width: 392px; height: 200px; }
  .tagline {
    position: absolute; left: 396px; top: 219px;
    font-family: "Cinzel", serif; font-size: 11px; line-height: 1.05;
    color: #fff; text-transform: uppercase;
  }
  .wordmark {
    position: absolute; left: 0; top: 38px; width: 196px; text-align: center;
    font-family: "Crimson Text", serif; font-weight: 400; color: var(--ink-plum);
  }
  .wordmark__name { font-size: 19px; letter-spacing: .5px; text-transform: uppercase; line-height: 1; }
  .wordmark__line { font-size: 12px; line-height: 1.05; }

  .contact {
    position: absolute; left: 0; top: 322px; width: 196px; text-align: center;
    font-family: "Crimson Text", serif; color: var(--ink-plum);
  }
  .contact__label { font-size: 9px; font-weight: 600; }
  .contact__email { font-size: 8px; margin-bottom: 9px; }
  .contact__web { font-size: 9px; letter-spacing: .6px; }
  .contact__phone { font-size: 17px; display: flex; align-items: center; justify-content: center; gap: 4px; line-height: 1; }
  .contact__phone svg { width: 15px; height: 15px; }

  .location { position: absolute; left: 0; top: 322px; width: 196px; }
  .location .copy { font-size: 5.8px; }

  /* inside spread */
  .about-title { font-size: 13px; font-weight: 700; color: #fff; padding: 14px 6px 4px; }
  .copy--indent { padding-left: 72px; text-align: right; }

  .price-list { width: calc(100% - 12px); margin: 0 6px 5px; font-size: 5.6px; border-collapse: collapse; }
  .price-list th { text-align: left; font-weight: 700; padding-top: 3px; }
  .price-list td { line-height: 1.3; }
  .price-list td:last-child { text-align: left; width: 46%; }

  .credentials {
    position: absolute; left: 70px; top: 338px; width: 244px; height: 54px;
    background: var(--green); border-radius: 4px; display: flex; gap: 10px;
    padding: 5px 7px; color: #fff; font-size: 5.2px; line-height: 1.3;
  }
  .credentials__col { flex: 1; }
  .credentials__col strong { display: block; font-weight: 700; }

  .footer-band {
    position: absolute; left: 196px; bottom: 0; width: 392px; height: 17px;
    background: var(--green); display: flex; align-items: center; color: #fff;
  }
  .footer-band__web { width: 196px; text-align: center; font-family: "Crimson Text", serif; font-size: 7px; letter-spacing: .5px; }
  .footer-band__phone { width: 196px; display: flex; justify-content: center; align-items: center; gap: 3px; font-family: "Crimson Text", serif; font-size: 11px; }
  .footer-band__phone svg { width: 10px; height: 10px; }

  .bullets { list-style: none; padding: 0 6px 0 10px; font-size: 5.6px; line-height: 1.3; margin-bottom: 4px; }
  .bullets li::before { content: "\25CF"; color: var(--green); margin: 0 3px 0 -6px; font-size: 4.5px; }
</style>
</head>
<body>
<main class="canvas">

  <!-- Outside of the trifold -->
  <section class="spread spread--outside">
    <article class="panel panel--plum">
      <div class="photo photo--lounge" role="img" aria-label="Photo of a black leather recliner chair in a calm therapy room"></div>
      <h2 class="band-heading">What is hypnotherapy?</h2>
      <p class="copy">What comes to mind? You may conjure up images or thoughts of stage shows. In reality, real hypnosis bears little resemblance to that and can be far more beneficial. It's all about slowing down the pace of life in order to allow your mind to receive positive suggestions for change. You've probably already experienced something similar to hypnosis and not even known it. Have you ever been on a train journey, sat there with half-closed eyes, day-dreaming or driven a journey and suddenly wonder how you reached your destination? In that boundary between sleep and awake our brain produces alpha waves – that's where I can help guide your unconscious mind to solve the problems that your conscious brain can't do on its own.</p>
      <h2 class="band-heading">What do I do as the hypnotherapist?</h2>
      <p class="copy">Hypnotherapy is a very relaxing process and it is my role to provide a safe and trusted environment where you can allow yourself to relax and slow down your mind. I do this through recognised relaxation techniques which then allow you to focus on the story I take you through, with the appropriate personalisation and suggestions included.</p>
      <h2 class="band-heading">What's it useful for?</h2>
      <p class="copy">I can carry out short term (1-3 sessions) tailored hypnotherapy which is useful for a wide range of areas as listed in the box on the right of this screen. I am also able, in longer term work, to provide Hypnotherapy in conjunction with counselling or other techniques as is appropriate for you.</p>
      <p class="copy"><em>Cost: £40 per one hour session</em></p>
      <p class="copy"><strong>Hypnotherapy Service</strong><br>Stopping smoking, Phobia cure, Nerves, anxiety and worry, Stress reduction and management, Exam nerves, Irritation and agitation, Headaches, Relaxation, Weight control, Teeth grinding, Motivation, Pain relief / management, Positive thinking, Memory, Sleep issues and Insomnia, Self-esteem and confidence, Habit elimination / reduction, Sports Performance Enhancement</p>
    </article>

    <article class="panel panel--plum">
      <div class="location">
        <p class="copy">I'm situated behind Brightcut hairdresser and Milton's fish and chip shop. The entrance door is white with my Larkmore Counselling &amp; Hypnotherapy sign on it.<br>Please note, I am on the first floor and there are eight stairs up into the counselling room.<br>There is no waiting room so please arrive at the agreed time.<br>You can contact me as follows:</p>
        <p class="copy"><strong>Postal and location address:<br>Larkmore Counselling and Hypnotherapy.<br>4b Harbour Lane.<br>Eastmere.<br>EM4 2QT</strong></p>
      </div>
    </article>

    <article class="panel panel--paper">
      <div class="wordmark">
        <div class="wordmark__name">Larkmore</div>
        <div class="wordmark__line">Counselling &amp;</div>
        <div class="wordmark__line">Hypnotherapy</div>
      </div>
      <div class="contact">
        <div class="contact__label">Email</div>
        <div class="contact__email">larkmoretherapy@mailbox.co.uk</div>
        <div class="contact__web">www.larkmoretherapy.co.uk</div>
        <div class="contact__phone">
          <svg viewBox="0 0 20 20" aria-hidden="true"><circle cx="10" cy="10" r="9" fill="none" stroke="currentColor" stroke-width="1.6"/><path d="M7 5.5c.6-.4 1.2-.3 1.5.2l.9 1.6c.3.5.1 1-.3 1.3l-.6.4c.5 1.2 1.4 2.1 2.6 2.6l.4-.6c.3-.4.8-.6 1.3-.3l1.6.9c.5.3.6.9.2 1.5-.6.9-1.6 1.2-2.6.8-2.6-1-4.6-3-5.6-5.6-.4-1 0-2 .6-2.8z" fill="currentColor"/></svg>
          <span>07700 900415</span>
        </div>
      </div>
    </article>

    <svg class="wave-art" viewBox="0 0 392 200" aria-hidden="false">
      <defs>
        <linearGradient id="shoreGradient" x1="0" y1="0" x2="0" y2="1">
          <stop offset="0" stop-color="#a99c88"/>
          <stop offset=".45" stop-color="#e3cfa8"/>
          <stop offset=".6" stop-color="#7d7468"/>
          <stop offset="1" stop-color="#2e2a29"/>
        </linearGradient>
      </defs>
      <path d="M196 22 C270 4 330 2 392 6 L392 30 C330 26 270 30 196 44 Z" fill="#7a4f7d"/>
      <path d="M196 18 C270 0 330 -2 392 2" fill="none" stroke="#2f9d45" stroke-width="2"/>
      <path d="M0 44 C120 30 250 22 392 30 L392 150 C260 166 120 160 0 146 Z" fill="url(#shoreGradient)" role="img" aria-label="Photo of a family walking hand in hand along a beach at sunset"/>
      <path d="M0 146 C120 160 260 166 392 150 L392 170 C260 184 120 178 0 162 Z" fill="#5e3a61"/>
      <path d="M0 166 C120 182 260 188 392 174" fill="none" stroke="#2f9d45" stroke-width="2"/>
    </svg>
    <p class="tagline">Trusted Professional<br>An approach tailored<br>to you</p>
  </section>

  <!-- Inside of the trifold -->
  <section class="spread spread--inside">
    <article class="panel panel--plum">
      <h1 class="about-title">About ME</h1>
      <p class="copy">There are times in all of our lives when we feel we have lost our way, we need a listening ear or we simply want somebody to work together with to help us reach the next step in our journey, whatever that may be. Maybe that sounds like you and you're looking for somebody to help you take that first step or maybe you simply want somebody to share your concerns with and really feel heard.</p>
      <p class="copy">I am a fully qualified counsellor and I'm able to provide a safe, confidential environment for you to speak, to feel, to be heard and valued as an individual in what can be a scary and challenging world.</p>
      <p class="copy">I have experience of working with people with a wide range of concerns. Some examples include loss and grief, depression, anxiety, relationships, self-esteem, eating disorders, confidence, general personal development and growth. I find this work really rewarding and it's been a privilege to work with all of these people.</p>
      <p class="copy">My main way of working is based on the Transactional Analysis model and I also able to use a wide range of techniques and theories, tailoring my approach to suit you. Some examples include NLP, CBT, EFT, Mindfulness, creative sand-tray. If you'd like to understand more about these and other techniques I may use then just take a look here.</p>
      <p class="copy copy--indent">In addition to a more typical counselling role, I am able to offer hypnotherapy. I find this works really well in combination with counselling. I am also happy to offer this on its own for specific things such as giving up smoking, phobias, relaxation, confidence and much more.</p>
      <p class="copy copy--indent">I'm happy to support individuals over fourteen years of age and couples on a face-to-face basis for short, medium or long term therapy.</p>
      <div class="photo photo--portrait" role="img" aria-label="Portrait photo of the counsellor smiling, wearing a red top"></div>
    </article>

    <article class="panel panel--plum">
      <h2 class="band-heading band-heading--soft">How much will it cost me?</h2>
      <table class="price-list">
        <tr><th colspan="2">Individual counselling:</th></tr>
        <tr><td>Initial assessment session</td><td>- £15 (50 mins)</td></tr>
        <tr><td>On-going sessions</td><td>- £30 (1 hour)</td></tr>
        <tr><th>Hypnotherapy</th><td>- £40 (1 hour)</td></tr>
        <tr><th colspan="2">Couples</th></tr>
        <tr><td>Initial assessment session</td><td>- £40 (1 hour)</td></tr>
        <tr><td>Ongoing sessions</td><td>- £60 (1 ½ hours)</td></tr>
        <tr><th>Group</th><td>- £20 per person (1 ½ hours)</td></tr>
      </table>
      <p class="copy">I have a limited amount of low cost counselling spaces. These are for people in individual counselling only who are currently not in employment.</p>
      <p class="copy">In exceptional circumstances I am able to offer home visits, additional mileage will be charged in these instances of 45p per mile.</p>
      <p class="copy">I prefer payment by cash, credit / debit card or electronic transfer. For card payments a £1 handling fee will be added.</p>
      <p class="copy"><strong>What if I have to cancel an appointment?</strong></p>
      <p class="copy">Cancellations within 24 hours will be charged at the full rate. Cancellations outside of 24 hours and within 48 hours will be charged at 50%<br>Outside of 48 hours no fee will be charged.</p>
    </article>

    <article class="panel panel--plum">
      <div class="photo photo--room" role="img" aria-label="Photo of a bright counselling room with a cream sofa and cushions"></div>
      <h2 class="band-heading">What is counselling?</h2>
      <p class="copy">It's about being able to have a safe and trusted environment where you feel comfortable to share whatever is going on for you, problems, concerns, areas you'd like to personally develop. Essentially, it's time for you to just be you, free from any form of judgement.</p>
      <h2 class="band-heading">What do I do as the counsellor?</h2>
      <p class="copy">My key skill is in listening...that's really listening and hearing, seeing you, empathising with your feelings. It's then my role to facilitate you in finding your own solutions and in helping you increase your own self-awareness and realisation that you have choices.</p>
      <h2 class="band-heading">What's transactional analysis?</h2>
      <p class="copy">Transactional Analysis (TA) is the core method behind my overall counselling approach. It dates back to the 1960's, its founder being Alden Marsh, a Canadian born Psychiatrist and Psychotherapist. It's a proven theory of personality and a therapy focused on personal growth and change. The core beliefs that underpin the approach are:</p>
      <ul class="bullets">
        <li>People are OK (each person has validity, importance and equality in respect).</li>
        <li>Everyone has the capacity to think (with few exceptions, such as severe brain damage)</li>
        <li>People have choices and are able to decide their destiny.</li>
      </ul>
      <p class="copy">It was Marsh's belief that we make "survival decisions" as small children which result in how we see, think and feel about ourselves and others in the world. Those decisions were useful to us at the time but carried into our adult life, they may not always serve us well. We can work together to understand what is useful and what isn't, with the opportunity to explore other choices.</p>
      <p class="copy"><em>Cost: £30 per one hour session.</em></p>
      <p class="copy"><strong>Counselling Service</strong><br>Grief and Loss, Anxiety, Depression, Stress, Relationships, Self esteem, Confidence, Personal development, Self harm, Sexual concerns, Eating disorders, Abuse</p>
    </article>

    <aside class="credentials">
      <div class="credentials__col">
        <strong>Qualifications &amp; Memberships</strong>
        Diploma in Counselling<br>Diploma in Hypnotherapy<br>Diploma in Management<br>Diploma in NLP<br>BA (Hons) Education and Research
      </div>
      <div class="credentials__col">
        <strong>Member of:</strong>
        ACPR (Member)<br>TAPA (Member)<br>Northern Counselling Guild<br>Guild of Clinical Hypnotherapy (Member)<br><br>Fully insured and CRB checked.<br>Data Protection Registered.
      </div>
    </aside>

    <footer class="footer-band">
      <span class="footer-band__web">www.larkmoretherapy.co.uk</span>
      <span class="footer-band__phone">
        <svg viewBox="0 0 20 20" aria-hidden="true"><circle cx="10" cy="10" r="9" fill="none" stroke="currentColor" stroke-width="1.6"/><path d="M7 5.5c.6-.4 1.2-.3 1.5.2l.9 1.6c.3.5.1 1-.3 1.3l-.6.4c.5 1.2 1.4 2.1 2.6 2.6l.4-.6c.3-.4.8-.6 1.3-.3l1.6.9c.5.3.6.9.2 1.5-.6.9-1.6 1.2-2.6.8-2.6-1-4.6-3-5.6-5.6-.4-1 0-2 .6-2.8z" fill="currentColor"/></svg>
        07700 900415
      </span>
    </footer>
  </section>

</main>
</body>
</html>
```